OLU58 biz card & Stationery

LU58 is a personalized shopping experience brought to you, that lets you find and discover fashion goods through a collection of boutiques curated by taste-makers - celebrities, stylists, designers, and fashion bloggers. Boutiques uses visual technology to help fashionistas discover and shop their look and creates the opportunity for designers to showcase their collections and latest inspirations online.

OLU58 is built on technology developed by our team of fashion experts who work with engineers to “teach” our computer systems to understand various patterns, pairings, and genre definitions. When signed into your account, OLU58 learns about your style and preferences and in turn, provides you better results and recommendations over time. Ultimately, OLU58 will provide shoppers with a much richer and interactive shopping experience and help drive traffic to retailers' websites.

We need a definitely cool business card. The card must be black! And must use our official logo which can be download from OLU58.com

The address for Letter head and evenlop, please use 4872 Crestwick Parkway, Sutie 510 Los Angeles CA90412, email will be anyone@OLU58.com, website is www.OLU58.com

thanks

We received some of the design, thanks. But most of the design are not what we want. We need a very clean version with black ground, you may also use some dark gray to add the element. please take a look at http://morvalstudio.no/work/#pelter__ostrama/, we do like this kind of design very much. hope it help.

```html
<!DOCTYPE html>
<html lang="en">
<head>
<meta charset="utf-8">
<title>OLU58 Business Card</title>
<link rel="stylesheet" href="https://fonts.googleapis.com/css2?family=Marcellus&family=Roboto+Condensed:wght@400&display=swap">
<style>
  :root {
    --page: #ffffff;
    --card: #000000;
    --band: #5c5c5d;
    --ink: #ffffff;
    --band-ink: #e6e6e6;
    --shadow: rgba(0, 0, 0, 0.45);
  }
  * { margin: 0; padding: 0; box-sizing: border-box; }
  html, body {
    width: 1200px;
    height: 900px;
    overflow: hidden;
    background: var(--page);
  }
  .sheet {
    position: relative;
    width: 1200px;
    height: 900px;
  }
  .card {
    position: absolute;
    left: 231px;
    width: 737px;
    height: 371px;
    background: var(--card);
    overflow: hidden;
    box-shadow: 3px 3px 4px var(--shadow);
  }
  .card--front { top: 62px; }
  .card--back { top: 472px; }

  .brand-name {
    position: absolute;
    left: -5px;
    top: 174px;
    font-family: "Marcellus", serif;
    font-size: 128px;
    line-height: 1;
    color: var(--ink);
    letter-spacing: 1px;
    white-space: nowrap;
  }
  .tagline-band {
    position: absolute;
    left: 636px;
    top: 0;
    width: 56px;
    height: 100%;
    background: var(--band);
    display: flex;
    align-items: center;
    justify-content: center;
  }
  .tagline {
    writing-mode: vertical-rl;
    transform: rotate(180deg);
    font-family: "Marcellus", serif;
    font-size: 19px;
    letter-spacing: 1.5px;
    color: var(--band-ink);
    white-space: nowrap;
  }

  .contact {
    position: absolute;
    left: 18px;
    bottom: 16px;
    writing-mode: vertical-rl;
    transform: rotate(180deg);
    font-family: "Roboto Condensed", sans-serif;
    font-size: 21px;
    line-height: 32px;
    color: var(--ink);
    white-space: nowrap;
  }
  .website {
    position: absolute;
    left: 262px;
    top: 230px;
    font-family: "Marcellus", serif;
    font-size: 56px;
    line-height: 1;
    color: var(--ink);
    white-space: nowrap;
  }
</style>
</head>
<body>
  <main class="sheet">
    <section class="card card--front" aria-label="Business card front">
      <h1 class="brand-name">OLU58</h1>
      <div class="tagline-band">
        <p class="tagline">SOCIAL FASHION ONLINE</p>
      </div>
    </section>
    <section class="card card--back" aria-label="Business card back">
      <address class="contact">
        4872 Crestwick Parkway,<br>
        Sutie 510 Los Angeles CA90412<br>
        anyone@OLU58.com
      </address>
      <p class="website">www.OLU58.com</p>
    </section>
  </main>
</body>
</html>
```